BRW (Miriela Vondrash Wellness) Website supporting women to live a healthy lifestyle

Hi
I'm thrilled to be working together to bring a fresh look to my website! As an Integrative Health Practitioner, my mission is to support and empower women on their journey to reclaim their health and well-being. The website should feel inviting, with a soft and nurturing energy that also radiates vibrancy and vitality.

Design & Aesthetic:

I'd love to focus on rich rose gold tones
It should feel soft and approachable yet energetic and lively.

Functional Needs:

The site will support both my coaching services
and product sales, so it’s essential to have an intuitive and user-friendly shopping experience.
I'd love some exciting interactive features that keep visitors engaged and make the journey through the site feel seamless and uplifting.

Please let me know if there’s any additional information you need from me to bring this vision to life!

Thank you for your attention to these details! Here are some ideas I like to see Layout Ideas

Hero Section: An inviting header with a subtle half-moon background for a touch of healing energy.

Navigation & Logo: Place my logo in gold on the top left and use simple navigation links with a rose gold hover effect.

Section Dividers: Use small celestial icons, like a crescent moon, as dividers to create flow and add a bit of magic.

Product & Service Section: A soft rose gold gradient background to highlight products, with circular or wave accents around images.

Footer: Deep rose gold background with a half-moon icon to end with a warm invitation to connect.

Uploading an AI-generated image (it is a bit over the top but it captures the feel I like), with a hint of spirituality and femininity, along with elements like the half moon and colors. :) I'm also uploading my logos, and I have each option available in both color schemes.

Best,
Miriela

• Playfair Display (Headings) & Lora (Body Text)

• Cartwell

```html
<!DOCTYPE html>
<html lang="en">
<head>
<meta charset="utf-8">
<title>BRW — Miriela Vondrash Wellness</title>
<link rel="stylesheet" href="https://fonts.googleapis.com/css2?family=Playfair+Display:wght@400;500&family=Lora:wght@400;500&family=Poppins:wght@400;500;600&display=swap">
<style>
:root{
  --ink:#1c1b1a;
  --muted:#5b5551;
  --peach:#f9bd92;
  --peach-btn:#f8c3a0;
  --blush:#fde9dc;
  --card:#fbe5d6;
  --rose:#e3a98b;
  --line:#e7d6cc;
  --black:#000;
  --white:#fff;
}
*{margin:0;padding:0;box-sizing:border-box}
html,body{width:1200px;height:3259px;overflow:hidden}
body{position:relative;background:var(--white);color:var(--ink);font-family:"Lora",serif}
.abs{position:absolute}
.serif{font-family:"Playfair Display",serif;font-weight:400}
.sans{font-family:"Poppins",sans-serif}

/* header */
.hero{position:absolute;left:0;top:0;width:1200px;height:650px;
  background:radial-gradient(ellipse 700px 500px at 0 0,#fbd9c2 0%,#fdeee4 45%,#fff 80%)}
.brand{left:183px;top:18px;display:flex;align-items:center;gap:10px;height:56px}
.brand-dot{width:14px;height:14px;border-radius:50%;background:var(--ink)}
.brand-name{font-family:"Lora",serif;font-size:26px;color:var(--ink);letter-spacing:1px}
.nav{left:318px;top:36px;display:flex;gap:34px;font-size:12px}
.nav a{color:var(--ink);text-decoration:none}
.nav .active{border-bottom:1px solid var(--ink);padding-bottom:6px}
.phone{left:660px;top:36px;font-size:12px;display:flex;align-items:center;gap:8px}
.btn-black{left:771px;top:28px;width:106px;height:34px;background:var(--black);color:#fff;font-size:11px;display:flex;align-items:center;justify-content:center}
.btn-peach-sm{left:890px;top:28px;width:128px;height:34px;background:var(--peach-btn);font-size:11px;display:flex;align-items:center;justify-content:center}

.hero-title{left:183px;top:148px;font-size:55px;line-height:58px;width:520px;white-space:nowrap}
.hero-text{left:183px;top:340px;width:390px;font-size:13.5px;line-height:20.5px;color:var(--muted)}
.checks{left:183px;top:420px;list-style:none;font-size:13.5px}
.checks li{display:flex;align-items:center;gap:14px;height:31px}
.tick{width:17px;height:17px;border-radius:50%;background:#f0a98a;display:flex;align-items:center;justify-content:center}
.cta{top:530px;height:41px;font-size:12.5px;display:flex;align-items:center;justify-content:center}
.cta-fill{left:183px;width:196px;background:var(--peach-btn)}
.cta-line{left:390px;width:195px;border:1px solid var(--peach-btn);background:#fff}
.arch-outline{left:673px;top:143px;width:345px;height:455px;border:1px solid #ecd3c4;border-bottom:none;border-radius:173px 173px 0 0}
.hero-photo{left:690px;top:100px;width:328px;height:498px;border-radius:164px 164px 0 0;
  background:linear-gradient(180deg,#f9bd92 0%,#f6b58a 55%,#7d7564 82%,#4c4a43 100%)}

/* stats */
.stats{left:0;top:650px;width:1200px;height:134px;background:var(--black);color:#fff}
.stat{position:absolute;top:28px;text-align:center;font-family:"Poppins",sans-serif}
.stat-num{font-size:44px;font-weight:600;line-height:48px;display:flex;align-items:center;gap:10px;justify-content:center}
.stat-num i{width:22px;height:22px;border:2px solid #fff;border-radius:50%;display:inline-block}
.stat-lbl{font-size:14px;margin-top:2px}
.stat-div{position:absolute;top:25px;width:1px;height:80px;background:#333}

/* about */
.about-arch-line{left:198px;top:843px;width:330px;height:489px;border:1px solid var(--line);border-bottom:none;border-radius:165px 165px 0 0}
.about-photo{left:183px;top:870px;width:330px;height:462px;border-radius:165px 165px 0 0;
  background:linear-gradient(180deg,#f3f0ec 0%,#e9d3c1 40%,#c98d6d 70%,#6d6a4c 100%)}
.accent-leaf{left:50px;top:890px;width:95px;height:95px;border-radius:50% 0 50% 0;background:#e8a52a;opacity:.85}
.label{font-size:12px}
.about-label{left:602px;top:900px}
.about-title{left:599px;top:920px;font-size:40px;line-height:46px;white-space:nowrap}
.about-text{left:599px;top:1027px;width:405px;font-size:13.5px;line-height:20.5px;color:var(--muted)}
.btn-rose{left:599px;top:1274px;width:245px;height:42px;background:#f0ad8e;font-size:12.5px;display:flex;align-items:center;justify-content:center}
.lotus-faint{left:990px;top:1235px;width:175px;height:115px;border-radius:90px 90px 20px 20px;background:#fdeee6}

/* services */
.services{left:0;top:1427px;width:1200px;height:666px;background:linear-gradient(180deg,#fdeee4 0%,#fff7f2 60%,#fff 100%)}
.eucalyptus{left:0;top:1418px;width:220px;height:128px;border-radius:60px 20px 60px 20px;background:linear-gradient(120deg,#6f9a7e,#a7c2ae);opacity:.85}
.center{left:0;width:1200px;text-align:center}
.svc-label{top:1515px}
.svc-title{top:1535px;font-size:40px;line-height:46px}
.card{position:absolute;top:1655px;width:252px;height:315px;background:var(--card);border-radius:126px 126px 0 0;text-align:center}
.card-icon{width:44px;height:44px;margin:58px auto 0;border-radius:50%;border:1.6px solid var(--ink)}
.card h3{font-family:"Lora",serif;font-weight:400;font-size:17.5px;line-height:22px;margin-top:32px}
.card p{font-size:12.5px;line-height:20.5px;color:var(--muted);margin:20px 20px 0}
.card a{display:inline-block;margin-top:14px;font-size:12.5px;color:var(--ink)}

/* reviews */
.rev-label{top:2172px}
.rev-title{top:2190px;font-size:40px;line-height:48px}
.quote-mark{left:187px;top:2318px;font-family:"Poppins",sans-serif;font-weight:600;font-size:44px;line-height:30px}
.quote-text{left:187px;top:2362px;width:400px;font-size:20px;line-height:31.7px}
.quote-by{left:187px;top:2664px;font-family:"Poppins",sans-serif;font-size:18px}
.rev-photo{left:631px;top:2275px;width:386px;height:437px;border-radius:193px 193px 0 0;
  background:linear-gradient(180deg,#c7dbe8 0%,#e9eef0 38%,#7ea9ae 55%,#b89878 75%,#d6b995 100%)}
.lotus-left{left:0;top:2530px;width:110px;height:120px;border-radius:0 60px 60px 0;background:#fdeee6}
.floral{left:1010px;top:2325px;width:110px;height:185px;border-radius:55px;background:#f4f1ef}

/* footer */
.footer{left:0;top:2843px;width:1200px;height:416px;background:var(--rose)}
.f-brand{left:183px;top:2990px;display:flex;align-items:center;gap:8px;font-size:15px;width:160px;justify-content:center}
.f-brand span.d{width:10px;height:10px;border-radius:50%;background:var(--ink);flex:none}
.f-brand-name{font-size:15px;line-height:18px;text-align:center}
.socials{left:191px;top:3057px;display:flex;gap:6px}
.socials span{width:23px;height:23px;border-radius:50%;background:#c99378}
.socials span:first-child{background:var(--black)}
.f-head{top:2946px;font-size:15px;font-weight:500}
.f-links{left:384px;top:2980px;list-style:none;font-size:13px;color:#5e4538}
.f-links li{height:27px}
.f-contact{left:555px;top:2980px;list-style:none;font-family:"Poppins",sans-serif;font-size:12.5px;color:#4d3a30}
.f-contact li{display:flex;gap:12px;margin-bottom:14px;line-height:16px}
.f-news{left:765px;top:2978px;width:260px;font-family:"Poppins",sans-serif;font-size:12px;line-height:17px;color:#5e4538}
.f-input{left:765px;top:3033px;width:201px;height:47px;background:#fff;font-family:"Poppins",sans-serif;font-size:10.5px;color:#8a8a8a;padding:18px 0 0 26px}
.f-go{left:966px;top:3033px;width:52px;height:47px;background:var(--black);display:flex;align-items:center;justify-content:center}
.f-rule{left:38px;top:3158px;width:1124px;height:1px;background:#d59a7d}
.f-small{top:3203px;font-family:"Poppins",sans-serif;font-size:11px;color:#3a2b23}
</style>
</head>
<body>

<section class="hero" aria-label="Hero"></section>
<header>
  <div class="abs brand"><span class="brand-dot"></span><span class="brand-name">BRW</span></div>
  <nav class="abs nav"><a class="active" href="#">Home</a><a href="#">About Me</a><a href="#">Coaching Services</a><a href="#">Blog</a></nav>
  <div class="abs phone"><svg width="12" height="12" viewBox="0 0 24 24"><path d="M6.6 10.8a15 15 0 0 0 6.6 6.6l2.2-2.2c.3-.3.7-.4 1-.2 1.1.4 2.3.6 3.6.6.6 0 1 .4 1 1V20c0 .6-.4 1-1 1A17 17 0 0 1 3 4c0-.6.4-1 1-1h3.5c.6 0 1 .4 1 1 0 1.3.2 2.5.6 3.6.1.3 0 .7-.2 1z" fill="#1c1b1a"/></svg>(555)-014-2286</div>
  <div class="abs btn-black">Instant Estimate</div>
  <div class="abs btn-peach-sm">Request Cancelation</div>
</header>

<h1 class="abs serif hero-title">Empowering<br>Women on Their<br>Health Journey</h1>
<p class="abs hero-text">As an Integrative Health Practitioner, I am dedicated to supporting women in reclaiming their health. With a holistic approach that blends ancient wisdom and modern science.</p>
<ul class="abs checks">
  <li><span class="tick"><svg width="9" height="9" viewBox="0 0 10 10"><path d="M1.5 5.2l2.3 2.3 4.7-5" stroke="#fff" stroke-width="1.5" fill="none"/></svg></span>Personalized Wellness Coaching</li>
  <li><span class="tick"><svg width="9" height="9" viewBox="0 0 10 10"><path d="M1.5 5.2l2.3 2.3 4.7-5" stroke="#fff" stroke-width="1.5" fill="none"/></svg></span>Nutrition Guidance</li>
  <li><span class="tick"><svg width="9" height="9" viewBox="0 0 10 10"><path d="M1.5 5.2l2.3 2.3 4.7-5" stroke="#fff" stroke-width="1.5" fill="none"/></svg></span>Mindfulness and Stress Management</li>
</ul>
<div class="abs cta cta-fill">24/7 Instant Quote Online</div>
<div class="abs cta cta-line">Request your consultation</div>
<div class="abs arch-outline"></div>
<div class="abs hero-photo" role="img" aria-label="Photo of a woman meditating cross-legged on a rock against a peach arch"></div>

<section class="abs stats" aria-label="Highlights">
  <div class="stat" style="left:183px;width:100px"><div class="stat-num"><i></i>5<small style="font-size:14px">★</small></div><div class="stat-lbl">Client Rating</div></div>
  <div class="stat-div" style="left:405px"></div>
  <div class="stat" style="left:525px;width:150px"><div class="stat-num"><i></i>20<small style="font-size:16px">+</small></div><div class="stat-lbl">Years of experience</div></div>
  <div class="stat-div" style="left:770px"></div>
  <div class="stat" style="left:828px;width:195px"><div class="stat-num"><i></i>20,000</div><div class="stat-lbl">Surgeries performed</div></div>
</section>

<div class="abs accent-leaf" role="img" aria-label="Golden leaf accent"></div>
<div class="abs about-arch-line"></div>
<div class="abs about-photo" role="img" aria-label="Photo of a smiling woman in a flowing peach dress at sunset"></div>
<p class="abs label about-label">About Us</p>
<h2 class="abs serif about-title">Empowering Wellness,<br>Inspiring Balance</h2>
<p class="abs about-text">An Integrative Health Practitioner with a passion for empowering women to reclaim their health and embrace a balanced, vibrant life. With a holistic approach rooted in both ancient wisdom and modern wellness practices, I'm dedicated to guiding you on a journey that nurtures the mind, body, and spirit. Through personalized coaching and wellness tools, I aim to support you in overcoming obstacles, achieving your goals, and rediscovering your natural vitality. Whether you're seeking to boost energy, improve nutrition, or reduce stress, my goal is to create a compassionate and supportive space where true transformation can thrive.</p>
<div class="abs btn-rose">Learn More About My Approach</div>
<div class="abs lotus-faint" role="img" aria-label="Faint lotus decoration"></div>

<section class="abs services" aria-label="Coaching Services"></section>
<div class="abs eucalyptus" role="img" aria-label="Eucalyptus branch"></div>
<p class="abs center label svc-label">Coaching Services</p>
<h2 class="abs center serif svc-title">Transformative Coaching for<br>Lasting Wellness</h2>
<article class="card" style="left:201px"><div class="card-icon"></div><h3>Personalized Wellness<br>Coaching</h3><p>This one-on-one coaching is tailored to meet your specific health and wellness goals.</p><a href="#">Learn More</a></article>
<article class="card" style="left:474px"><div class="card-icon"></div><h3>Nurture Your Body<br>with Mindful</h3><p>This service focuses on practical &amp; sustainable nutrition strategies to support you.</p><a href="#">Learn More</a></article>
<article class="card" style="left:748px"><div class="card-icon"></div><h3>Mindfulness and<br>Stress Management</h3><p>In today's fast-paced world, stress can be overwhelming, through mindfulness techniques.</p><a href="#">Learn More</a></article>

<p class="abs center label rev-label">Reviews</p>
<h2 class="abs center serif rev-title">What My Clients Are Saying</h2>
<div class="abs lotus-left" role="img" aria-label="Faint lotus decoration"></div>
<div class="abs quote-mark">”</div>
<p class="abs quote-text">Working with BRW has been life changing. She guided me with compassion and expertise, helping me feel empowered and healthy in ways I never thought possible! The mindfulness and nutrition strategies have truly transformed my daily life. I feel more energetic, balanced, and grounded. Thank you</p>
<p class="abs quote-by">— Danielle, 48</p>
<div class="abs rev-photo" role="img" aria-label="Photo of a wooden boardwalk railing overlooking the sea"></div>
<div class="abs floral" role="img" aria-label="Line-drawn floral sprig"></div>

<footer class="abs footer" aria-label="Footer"></footer>
<div class="abs f-brand"><span class="d"></span><span class="f-brand-name">Miriela Vondrash Wellness</span></div>
<div class="abs socials" aria-label="Social links"><span></span><span></span><span></span><span></span></div>
<h4 class="abs serif f-head" style="left:384px">Quick Links</h4>
<ul class="abs f-links"><li>Home</li><li>About Me</li><li>Coaching Services</li><li>Blog</li><li>Contact Us</li></ul>
<h4 class="abs serif f-head" style="left:555px">Contact Us</h4>
<ul class="abs f-contact">
  <li><svg width="12" height="12" viewBox="0 0 24 24"><path d="M6.6 10.8a15 15 0 0 0 6.6 6.6l2.2-2.2c.3-.3.7-.4 1-.2 1.1.4 2.3.6 3.6.6.6 0 1 .4 1 1V20c0 .6-.4 1-1 1A17 17 0 0 1 3 4c0-.6.4-1 1-1h3.5c.6 0 1 .4 1 1 0 1.3.2 2.5.6 3.6.1.3 0 .7-.2 1z" fill="#1c1b1a"/></svg>+ (555) 014 2286</li>
  <li><svg width="12" height="12" viewBox="0 0 24 24"><rect x="2" y="5" width="20" height="14" fill="#1c1b1a"/><path d="M2 5l10 8 10-8" stroke="#e3a98b" stroke-width="1.6" fill="none"/></svg>hello@brwellness.example</li>
  <li><svg width="12" height="14" viewBox="0 0 24 28"><path d="M12 1a9 9 0 0 0-9 9c0 7 9 17 9 17s9-10 9-17a9 9 0 0 0-9-9z" fill="#1c1b1a"/><circle cx="12" cy="10" r="3.2" fill="#e3a98b"/></svg>42 Linden Court,<br>Suite 8, Alderbrook</li>
</ul>
<h4 class="abs serif f-head" style="left:765px">Subscribe Our Newsletter</h4>
<p class="abs f-news">Unlock 10% off your first subscription when you sign up for our newsletter.</p>
<div class="abs f-input">Enter Email...</div>
<div class="abs f-go"><svg width="18" height="10" viewBox="0 0 18 10"><path d="M0 5h16M12 1l4 4-4 4" stroke="#fff" stroke-width="1.3" fill="none"/></svg></div>
<div class="abs f-rule"></div>
<p class="abs f-small" style="left:183px">Miriela Vondrash © All Rights Reserved.</p>
<p class="abs f-small" style="left:773px">Terms and Conditions</p>
<p class="abs f-small" style="left:942px">Privacy Policy</p>

</body>
</html>
```